Zerova Poultry "The Golden Crate"

I need a business card design and a logo design for my business. It's a delivery business of halal poultry (chicken). I would the business card to include the following information.
-business name: Zerova Poultry
-business tag line: "The Golden Crate"
Name: Tomas Velkor
Contact number: 07812450973
E-mail: zerova_fresh@mailvarn.com
Website: www.zerovapoultry.example
Also need a business logo also included relating to the business.
I would like it professional yet creative. Something original. I want it to have 2 main colours included.
I want it to have a middle Eastern/ Arabic look if possible.
Thanks :)
Target Market(s)
Butchers
Restaurants
Industry/Entity Type
Business
Contact Information for Business Card
Business name: Zerova poultry
Business tag line: "The Golden Crate"
E-mail: zerova_fresh@mailvarn.com
Name: Tomas Velkor
Look and feel

```html
<!DOCTYPE html>
<html lang="en">
<head>
<meta charset="utf-8">
<title>Zerova Poultry – Business Card</title>
<link rel="stylesheet" href="https://fonts.googleapis.com/css2?family=Tinos:ital,wght@0,400;1,400&family=Arimo:wght@400&display=swap">
<style>
  :root {
    --backdrop: #e4e6ea;
    --card: #ffffff;
    --brand-red: #d2070f;
    --brand-gold: #f2c218;
    --ink: #111111;
    --on-red: #ffffff;
  }
  * { margin: 0; padding: 0; box-sizing: border-box; }
  html, body {
    width: 1200px;
    height: 900px;
    overflow: hidden;
    background: var(--backdrop);
  }
  .business-card {
    position: absolute;
    left: 180px;
    top: 212px;
    width: 840px;
    height: 476px;
    background: var(--card);
    overflow: hidden;
    box-shadow: 0 6px 24px rgba(0, 0, 0, 0.18);
  }
  .accent-band {
    position: absolute;
    inset: 0;
    width: 840px;
    height: 476px;
  }
  .accent-band path { fill: var(--brand-red); }
  .brand {
    position: absolute;
    left: 40px;
    top: 92px;
    display: flex;
    align-items: center;
    gap: 14px;
  }
  .brand-mark {
    width: 96px;
    height: 96px;
    border-radius: 50%;
    background: var(--brand-gold);
  }
  .brand-text {
    display: flex;
    flex-direction: column;
    align-items: flex-end;
    margin-top: -34px;
  }
  .brand-name {
    font-family: "Tinos", "Times New Roman", serif;
    font-size: 36px;
    font-weight: 400;
    letter-spacing: 0.5px;
    color: var(--brand-red);
    line-height: 1;
    text-transform: uppercase;
  }
  .brand-tagline {
    font-family: "Tinos", "Times New Roman", serif;
    font-style: italic;
    font-size: 14px;
    color: var(--ink);
    line-height: 1.1;
    margin-top: 2px;
  }
  .holder-name {
    position: absolute;
    left: 150px;
    top: 262px;
    font-family: "Tinos", "Times New Roman", serif;
    font-size: 31px;
    font-weight: 400;
    color: var(--ink);
  }
  .contact-block {
    position: absolute;
    right: 24px;
    top: 232px;
    text-align: right;
    font-family: "Arimo", Arial, sans-serif;
    font-size: 17px;
    line-height: 22px;
    color: var(--on-red);
    font-style: normal;
    white-space: nowrap;
  }
</style>
</head>
<body>
  <article class="business-card">
    <svg class="accent-band" viewBox="0 0 840 476" aria-hidden="true">
      <path d="M840 150 C 600 220, 400 330, 260 476 L 840 476 Z"/>
    </svg>

    <header class="brand">
      <div class="brand-mark" aria-hidden="true"></div>
      <div class="brand-text">
        <span class="brand-name">Zerova Poultry</span>
        <span class="brand-tagline">The Golden Crate</span>
      </div>
    </header>

    <p class="holder-name">Tomas Velkor</p>

    <address class="contact-block">
      Suite 18<br>
      47 Marlow Row,<br>
      Tel: 07812450973<br>
      Email: zerova_fresh@mailvarn.com<br>
      www.zerovapoultry.example
    </address>
  </article>
</body>
</html>
```